Social Media Graphics - Copperfield Loop

Create 6-7 individual social media graphics (square size) to encourage folks to join our online course, using either of the text below (only one set of text per graphic:

The Lantern Ridge Method
How to Create a 7-Figure Business From Scratch
Sign Up Today!

Or

The Lantern Ridge Method
Fast-track Your Way to a Multi-Million Business!
Sign Up Today!

For the color scheme of the graphics, use 1 or 2 colors in the color palette attached; or use any colors that look nice with their outfits; AVOID using red, white and blue altogether because it will look like an Independence Day (4th of July) graphic and we don’t want that; make sure the graphics appeal to both men and women

Make sure each graphic contains 1 of the 2 pics attached; and make sure one of the graphics is all TEXT only.

Target Market(s)

men and women looking to make more money

Industry/Entity Type

entrepreneurship

Requirements
Must have
• see the text document attached
Nice to have
• We are open to a nice color design; the color palette colors are not required, especially we don't want red, white and blue used together
Should not have
• AVOID using red, white and blue altogether because it will look like an Independence Day (4th of July) graphic and we dont want that

```html
<!DOCTYPE html>
<html lang="en">
<head>
<meta charset="utf-8">
<title>The Lantern Ridge Method – Social Graphics</title>
<link rel="stylesheet" href="https://fonts.googleapis.com/css2?family=Oswald:wght@300;400;500;600;700&family=Montserrat:wght@400;500;700;800;900&display=swap">
<style>
  :root{
    --board:#46484b;
    --blush:#fbdcd9;
    --blush-deep:#f5c6cc;
    --rose:#efa9b8;
    --berry:#a8174a;
    --berry-bright:#d2386d;
    --navy:#12136e;
    --gold:#e3ad4a;
    --ink-light:#fdeee8;
    --photo-a:#23233a;
    --photo-b:#b8365a;
  }
  *{box-sizing:border-box;margin:0;padding:0}
  html,body{width:1200px;height:815px;overflow:hidden;background:var(--board)}
  .board{position:relative;width:1200px;height:815px;background:var(--board)}
  .card{position:absolute;width:331px;height:331px;background:var(--blush);overflow:hidden;box-shadow:0 4px 10px rgba(0,0,0,.45)}
  .card > *{position:absolute}
  .deco{left:0;top:0;width:331px;height:331px}
  .photo{background:linear-gradient(160deg,var(--photo-b) 0%,#7c2446 45%,var(--photo-a) 100%)}
  .photo.studio{background:linear-gradient(150deg,#d99aa6 0%,#3b2f3f 55%,#1c2150 100%)}
  .sans{font-family:"Montserrat",sans-serif}
  .cond{font-family:"Oswald",sans-serif}
  .btn{font-family:"Montserrat",sans-serif;font-weight:700;color:var(--ink-light);border-radius:20px;display:flex;align-items:center;justify-content:center;letter-spacing:.3px;box-shadow:1px 2px 3px rgba(0,0,0,.25);white-space:nowrap}
  .btn.navy{background:var(--navy)}
  .btn.berry{background:var(--berry)}
  .handle{display:flex;align-items:center;gap:4px;font-family:"Montserrat",sans-serif;font-weight:700;font-size:8px;color:var(--navy);white-space:nowrap}
  .handle .dot{width:9px;height:9px;border-radius:50%;background:var(--berry)}
  .tag{font-family:"Montserrat",sans-serif;color:var(--berry);text-transform:uppercase;text-align:right;line-height:1.35;white-space:nowrap}
  .nowrap{white-space:nowrap}
</style>
</head>
<body>
<main class="board">

  <!-- Card 1 -->
  <section class="card card-diamond" style="left:67px;top:58px">
    <svg class="deco" viewBox="0 0 331 331" aria-hidden="true">
      <rect x="0" y="0" width="60" height="120" fill="var(--ink-light)"/>
      <path d="M40 0 H200 L60 160 Z" fill="var(--blush-deep)"/>
      <path d="M110 0 L200 90 L55 250 L0 195 V0 Z" fill="none" stroke="var(--berry)" stroke-width="11" stroke-linejoin="round"/>
      <rect x="182" y="-18" width="60" height="60" rx="6" transform="rotate(45 212 12)" fill="none" stroke="var(--navy)" stroke-width="1.3"/>
      <rect x="172" y="-28" width="80" height="80" rx="8" transform="rotate(45 212 12)" fill="none" stroke="var(--berry)" stroke-width="1.3"/>
      <rect x="145" y="282" width="60" height="60" rx="6" transform="rotate(45 175 312)" fill="none" stroke="var(--navy)" stroke-width="1.6"/>
      <rect x="75" y="283" width="44" height="44" rx="5" transform="rotate(45 97 305)" fill="var(--berry)"/>
      <line x1="0" y1="253" x2="31" y2="278" stroke="var(--navy)" stroke-width="3" stroke-linecap="round"/>
      <line x1="156" y1="294" x2="196" y2="331" stroke="var(--berry)" stroke-width="3" stroke-linecap="round"/>
      <line x1="279" y1="55" x2="307" y2="55" stroke="var(--berry)" stroke-width="2"/>
      <rect x="313" y="26" width="5" height="5" transform="rotate(45 315 28)" fill="var(--gold)"/>
      <rect x="166" y="160" width="7" height="7" transform="rotate(45 169 163)" fill="var(--gold)"/>
      <circle cx="99" cy="236" r="1.6" fill="var(--navy)"/><circle cx="106" cy="236" r="1.6" fill="var(--navy)"/><circle cx="113" cy="236" r="1.6" fill="var(--navy)"/>
      <circle cx="289" cy="285" r="1.6" fill="var(--gold)"/><circle cx="296" cy="285" r="1.6" fill="var(--gold)"/><circle cx="303" cy="285" r="1.6" fill="var(--gold)"/>
    </svg>
    <div class="photo" role="img" aria-label="Photo of the two course hosts, arms crossed, smiling" style="left:0;top:26px;width:175px;height:225px;clip-path:polygon(0 0,100% 12%,62% 58%,22% 100%,0 100%)"></div>
    <div class="cond nowrap" style="right:24px;top:62px;font-size:34px;font-weight:500;color:var(--berry);line-height:1">THE</div>
    <div class="cond nowrap" style="right:24px;top:104px;font-size:32px;font-weight:700;color:var(--berry);line-height:1">LANTERN</div>
    <div class="cond nowrap" style="right:24px;top:146px;font-size:21px;font-weight:300;color:var(--navy);line-height:1;letter-spacing:2px">RIDGE</div>
    <div class="sans nowrap" style="right:24px;top:176px;font-size:23px;font-weight:800;color:var(--navy);line-height:1">METHOD</div>
    <div class="tag" style="right:25px;top:212px;font-size:9.5px;font-weight:500">How to create a 7-figure<br>business from scratch</div>
    <div class="btn navy" style="left:213px;top:253px;width:91px;height:19px;font-size:8.5px">SIGN UP TODAY!</div>
    <div class="handle" style="right:25px;top:298px"><span class="dot"></span>copperfieldloop</div>
  </section>

  <!-- Card 2 -->
  <section class="card card-blob" style="left:437px;top:58px">
    <svg class="deco" viewBox="0 0 331 331" aria-hidden="true">
      <path d="M180 0 H331 V90 C300 70 280 80 250 60 C210 40 190 30 180 0 Z" fill="var(--blush-deep)"/>
      <path d="M250 0 H331 V58 C310 65 300 50 295 35 C290 15 260 15 250 0 Z" fill="var(--berry-bright)"/>
      <path d="M0 120 C40 100 80 110 95 150 C110 190 140 200 150 230 C170 270 220 280 215 331 H0 Z" fill="var(--berry-bright)"/>
      <rect x="46" y="50" width="120" height="14" rx="7" transform="rotate(-38 106 57)" fill="none" stroke="var(--navy)" stroke-width="1.4"/>
      <rect x="80" y="60" width="150" height="18" rx="9" transform="rotate(-38 155 69)" fill="var(--rose)"/>
      <circle cx="161" cy="55" r="4" fill="none" stroke="var(--gold)" stroke-width="2"/>
      <path d="M103 87 l8 8 M111 87 l-8 8" stroke="var(--gold)" stroke-width="2"/>
      <path d="M254 18 v20 M244 28 h20" stroke="var(--ink-light)" stroke-width="1.5"/>
      <circle cx="282" cy="229" r="2" fill="var(--gold)"/><circle cx="295" cy="229" r="2" fill="var(--gold)"/><circle cx="308" cy="229" r="2" fill="var(--gold)"/>
    </svg>
    <div class="photo" role="img" aria-label="Photo of the two course hosts standing together, smiling" style="left:0;top:98px;width:162px;height:233px;border-radius:70px 70px 0 0"></div>
    <div class="sans" style="left:262px;top:40px;width:44px;height:44px;border-radius:50%;background:var(--navy);color:var(--ink-light);display:flex;align-items:center;justify-content:center;font-family:'Oswald',sans-serif;font-size:20px;font-weight:500">The</div>
    <div class="cond nowrap" style="right:18px;top:88px;font-size:40px;font-weight:700;color:var(--berry);line-height:1">LANTERN</div>
    <div class="cond nowrap" style="right:16px;top:134px;font-size:22px;font-weight:500;color:var(--berry);line-height:1">RIDGE</div>
    <div class="sans nowrap" style="right:16px;top:160px;font-size:21px;font-weight:800;color:var(--navy);line-height:1">METHOD</div>
    <div class="sans nowrap" style="right:16px;top:189px;font-size:9.5px;color:var(--berry);text-align:right;line-height:1.3">Fast-track Your Way<br>to a Multi-Million Business!</div>
    <div class="btn navy" style="left:222px;top:246px;width:90px;height:19px;font-size:8.5px">SIGN UP TODAY!</div>
    <div class="handle" style="right:18px;top:286px"><span class="dot"></span>copperfieldloop</div>
  </section>

  <!-- Card 3 -->
  <section class="card card-block" style="left:803px;top:58px">
    <svg class="deco" viewBox="0 0 331 331" aria-hidden="true">
      <g stroke="var(--ink-light)" stroke-width="1" opacity=".7">
        <line x1="240" y1="0" x2="331" y2="91"/><line x1="255" y1="0" x2="331" y2="76"/><line x1="270" y1="0" x2="331" y2="61"/><line x1="285" y1="0" x2="331" y2="46"/>
        <line x1="0" y1="270" x2="55" y2="325"/><line x1="0" y1="285" x2="46" y2="331"/><line x1="0" y1="300" x2="31" y2="331"/>
      </g>
      <circle cx="196" cy="34" r="9" fill="none" stroke="var(--gold)" stroke-width="1.3"/><circle cx="196" cy="34" r="4" fill="none" stroke="var(--gold)" stroke-width="1.3"/>
      <path d="M292 68 l8 7 l8 -7 M292 76 l8 7 l8 -7 M292 84 l8 7 l8 -7" fill="none" stroke="var(--berry)" stroke-width="1.6"/>
      <path d="M23 220 l8 -7 l8 7 M23 228 l8 -7 l8 7 M23 236 l8 -7 l8 7 M23 244 l8 -7 l8 7" fill="none" stroke="var(--navy)" stroke-width="1.6"/>
      <path d="M37 156 l10 10 M47 156 l-10 10" stroke="var(--gold)" stroke-width="1.5"/>
    </svg>
    <div class="cond nowrap" style="left:0;top:19px;width:138px;height:77px;background:var(--berry);border-radius:0 16px 0 0;color:var(--ink-light);font-size:30px;font-weight:700;display:flex;align-items:center;justify-content:center">LANTERN</div>
    <div class="cond nowrap" style="left:146px;top:16px;font-size:30px;font-weight:500;color:var(--berry);line-height:1">The</div>
    <div class="sans nowrap" style="left:146px;top:54px;font-size:32px;font-weight:900;color:var(--navy);line-height:1">RIDGE</div>
    <div class="sans nowrap" style="left:23px;top:106px;font-size:25px;font-weight:800;color:var(--navy);line-height:1">METHOD</div>
    <div class="photo studio" role="img" aria-label="Photo of the two course hosts in a gallery, smiling" style="left:54px;top:140px;width:277px;height:152px;border-radius:30px 0 0 0"></div>
    <div class="sans" style="left:236px;top:109px;width:62px;height:62px;border-radius:50%;background:var(--navy);border:4px solid var(--berry);color:var(--ink-light);display:flex;flex-direction:column;align-items:center;justify-content:center;line-height:1.05;text-align:center">
      <span class="cond" style="font-size:10px;font-weight:400">SIGN UP</span><span style="font-size:10px;font-weight:800">TODAY!</span>
    </div>
    <div class="sans nowrap" style="left:34px;top:274px;width:137px;height:31px;background:var(--berry-bright);color:var(--ink-light);font-size:8.5px;padding:5px 0 0 11px;line-height:1.35;box-shadow:1px 2px 3px rgba(0,0,0,.2)">Fast-track Your Way<br>to a Multi-Million Business!</div>
    <svg style="left:200px;top:280px;width:45px;height:20px" viewBox="0 0 45 20" aria-hidden="true">
      <circle cx="7" cy="4" r="2.5" fill="var(--gold)"/><circle cx="20" cy="4" r="2.5" fill="var(--gold)"/><circle cx="33" cy="4" r="2.5" fill="var(--gold)"/>
      <circle cx="7" cy="16" r="2.3" fill="none" stroke="var(--gold)"/><circle cx="20" cy="16" r="2.3" fill="none" stroke="var(--gold)"/><circle cx="33" cy="16" r="2.3" fill="none" stroke="var(--gold)"/>
    </svg>
    <div class="handle" style="right:16px;top:305px"><span class="dot"></span>copperfieldloop</div>
  </section>

  <!-- Card 4 -->
  <section class="card card-banner" style="left:67px;top:425px">
    <svg class="deco" viewBox="0 0 331 331" aria-hidden="true">
      <path d="M0 0 H150 V70 H60 C20 70 0 40 0 0 Z" fill="var(--blush-deep)" opacity=".7"/>
      <path d="M0 91 H95 Q128 91 128 124 V331 H0 Z" fill="var(--navy)"/>
      <path d="M16 104 l8 -7 l8 7 M16 112 l8 -7 l8 7 M16 120 l8 -7 l8 7 M16 128 l8 -7 l8 7" fill="none" stroke="var(--gold)" stroke-width="1.6"/>
      <circle cx="43" cy="44" r="5" fill="none" stroke="var(--gold)" stroke-width="2"/>
      <path d="M60 72 v8 M56 76 h8 M322 267 v8 M318 271 h8" stroke="var(--ink-light)" stroke-width="1.2"/>
      <path d="M224 292 l6 6 l-6 6 M231 292 l6 6 l-6 6 M238 292 l6 6 l-6 6" fill="none" stroke="var(--berry)" stroke-width="1.8"/>
      <circle cx="331" cy="331" r="32" fill="none" stroke="var(--navy)" stroke-width="14"/>
      <g stroke="var(--ink-light)" stroke-width="1" opacity=".7"><line x1="240" y1="331" x2="290" y2="281"/><line x1="255" y1="331" x2="300" y2="286"/><line x1="270" y1="331" x2="305" y2="296"/></g>
    </svg>
    <div class="cond nowrap" style="left:20px;top:12px;font-size:44px;font-weight:300;color:var(--berry);line-height:1">THE</div>
    <div class="cond nowrap" style="left:149px;top:0;width:182px;height:73px;background:var(--berry);border-radius:14px 0 0 14px;color:var(--ink-light);font-size:44px;font-weight:500;display:flex;align-items:center;justify-content:center">LANTERN</div>
    <div class="cond nowrap" style="right:15px;top:78px;font-size:29px;font-weight:700;color:var(--navy);line-height:1">RIDGE METHOD</div>
    <div class="photo" role="img" aria-label="Photo of the two course hosts, arms crossed, smiling" style="left:16px;top:114px;width:170px;height:217px;border-radius:80px 80px 0 0"></div>
    <div class="tag" style="right:16px;top:123px;font-size:11px;font-weight:500;line-height:1.55">How to<br>create a 7-figure<br>business from<br>scratch</div>
    <div class="btn berry" style="left:198px;top:208px;width:118px;height:23px;font-size:10.5px">SIGN UP TODAY!</div>
    <div class="handle" style="right:17px;top:249px"><span class="dot"></span>copperfieldloop</div>
  </section>

  <!-- Card 5 -->
  <section class="card card-arc" style="left:437px;top:425px">
    <svg class="deco" viewBox="0 0 331 331" aria-hidden="true">
      <path d="M100 40 C150 20 220 30 331 20 V220 C280 240 220 200 190 230 C150 260 120 200 100 150 Z" fill="var(--blush-deep)" opacity=".8"/>
      <circle cx="0" cy="0" r="26" fill="none" stroke="var(--navy)" stroke-width="12"/>
      <path d="M78 22 l6 6 l-6 6 M85 22 l6 6 l-6 6 M92 22 l6 6 l-6 6 M99 22 l6 6 l-6 6" fill="none" stroke="var(--berry)" stroke-width="1.8"/>
      <path d="M44 58 v14 M37 65 h14 M197 288 v14 M190 295 h14" stroke="var(--ink-light)" stroke-width="1.6"/>
      <path d="M0 112 A120 120 0 0 1 195 210 C200 250 170 290 150 331" fill="none" stroke="var(--berry)" stroke-width="2"/>
      <circle cx="276" cy="331" r="30" fill="none" stroke="var(--navy)" stroke-width="12"/>
      <line x1="283" y1="106" x2="310" y2="106" stroke="var(--navy)" stroke-width="3"/>
    </svg>
    <div class="photo" role="img" aria-label="Photo of the two course hosts, arms crossed, smiling" style="left:0;top:124px;width:170px;height:207px;border-radius:0 100px 0 0"></div>
    <div class="cond nowrap" style="right:21px;top:18px;font-size:28px;font-weight:300;color:var(--berry);line-height:1.1">THE LANTERN RIDGE</div>
    <div class="cond nowrap" style="right:20px;top:56px;font-size:40px;font-weight:700;color:var(--navy);line-height:1">METHOD</div>
    <div class="cond nowrap" style="right:21px;top:122px;font-size:15.5px;font-weight:400;color:var(--berry);text-align:right;line-height:1.38">FAST-TRACK<br>YOUR WAY TO A<br>MULTI-MILLION<br>BUSINESS!</div>
    <div class="btn navy" style="left:211px;top:232px;width:100px;height:21px;font-size:9px">SIGN UP TODAY!</div>
    <div class="handle" style="right:21px;top:276px"><span class="dot"></span>copperfieldloop</div>
  </section>

  <!-- Card 6 : text only -->
  <section class="card card-frame" style="left:803px;top:425px">
    <svg class="deco" viewBox="0 0 331 331" aria-hidden="true">
      <path d="M0 260 C60 240 120 290 200 270 C260 255 300 280 331 270 V331 H0 Z" fill="var(--blush-deep)" opacity=".6"/>
      <path d="M284 12 l6 6 l-6 6 M291 12 l6 6 l-6 6 M298 12 l6 6 l-6 6 M305 12 l6 6 l-6 6" fill="none" stroke="var(--gold)" stroke-width="1.6"/>
      <rect x="0" y="85" width="240" height="190" fill="var(--blush-deep)"/>
      <rect x="-2" y="74" width="252" height="190" fill="none" stroke="var(--berry)" stroke-width="2"/>
      <path d="M315 75 v9 M310.5 79.5 h9" stroke="var(--ink-light)" stroke-width="1.3"/>
      <circle cx="203" cy="86" r="4.5" fill="var(--blush)" stroke="var(--gold)" stroke-width="1.6"/>
      <path d="M25 264 v8 M21 268 h8" stroke="var(--navy)" stroke-width="1.3"/>
      <line x1="20" y1="112" x2="60" y2="112" stroke="var(--navy)" stroke-width="3"/>
    </svg>
    <div class="sans nowrap" style="left:0;top:19px;width:253px;height:46px;background:var(--navy);color:var(--blush);font-size:19px;font-weight:900;display:flex;align-items:center;padding-left:9px;letter-spacing:.2px">THE LANTERN RIDGE</div>
    <div class="handle" style="left:259px;top:39px;font-size:6.5px;gap:3px"><span class="dot" style="width:6px;height:6px"></span>copperfieldloop</div>
    <div class="cond nowrap" style="left:20px;top:124px;font-size:25px;font-weight:500;color:var(--navy);line-height:1.22;text-transform:uppercase">How to create<br>a 7-figure<br>business from<br><span style="color:var(--berry)">scratch</span></div>
    <div class="cond nowrap" style="left:286px;top:170px;transform:translate(-50%,-50%) rotate(-90deg);font-size:40px;font-weight:300;color:var(--berry);line-height:1">METHOD</div>
    <div class="btn navy" style="left:187px;top:288px;width:117px;height:25px;font-size:10.5px">SIGN UP TODAY!</div>
  </section>

</main>
</body>
</html>
```